Dallow Equipment requires a design to be used for stickers that will go on all new Excavators sold.

Design a sticker to include Dallow Equipment, want to use current corporate colours (Black and Red) but also incorporate the colour of the excavators we are selling so sticker looks in place and not cheap. We are happy at looking at modernising the Dallow Equipment logo particularly font or writing style to suit earthmoving equipment (strong, tough). Interested in new ideas so not necessarily your standard square or rectangle shape.
Text would be :
Sold and Serviced by
DALLOW EQUIPMENT
SALES-PARTS-SERVICE-RENTALS
Ph 1300 47 82 61
www.dallowplantco.example
Dallow Equipment would be dominate and largest, then phone number and reducing font quite a lot for other items

Target Market(s)

Earthmoving - so modern and hard, strong look

Requirements
Must have
• All items of text

```html
<!DOCTYPE html>
<html lang="en">
<head>
<meta charset="utf-8">
<title>Dallow Equipment – Sticker Concepts</title>
<link rel="stylesheet" href="https://fonts.googleapis.com/css2?family=Jost:wght@800&family=Open+Sans:wght@400;700&display=swap">
<style>
  :root {
    --ink: #0d0d0d;
    --brand-red: #e4202a;
    --excavator-teal: #16adbd;
    --paper: #ffffff;
  }
  html, body {
    margin: 0;
    padding: 0;
    width: 1200px;
    height: 591px;
    overflow: hidden;
    background: var(--paper);
  }
  .board { display: block; width: 1200px; height: 591px; }
  .wordmark-name { font-family: "Jost", "Arial Black", sans-serif; font-weight: 800; fill: var(--ink); }
  .body-text { font-family: "Open Sans", Arial, sans-serif; }
  .option-number { font-family: "Open Sans", Arial, sans-serif; font-size: 16px; fill: var(--ink); }
  .divider { stroke: var(--ink); stroke-width: 3; }
  .ring-outer { fill: var(--ink); }
  .ring-teal { fill: var(--excavator-teal); }
  .face-white { fill: var(--paper); }
  .face-teal { fill: var(--excavator-teal); }
  .ring-black { fill: none; stroke: var(--ink); }
  .orbit-line { fill: none; stroke: var(--ink); stroke-width: 1.5; }
  .tagline-dark { fill: var(--ink); }
  .tagline-light { fill: var(--paper); }
  .phone-dark { fill: var(--ink); font-weight: 700; }
  .phone-light { fill: var(--paper); font-weight: 700; }
  .orbit-text { font-family: "Open Sans", Arial, sans-serif; font-size: 16px; fill: var(--ink); }
</style>
</head>
<body>
<svg class="board" viewBox="0 0 1366 673" xmlns="http://www.w3.org/2000/svg">
  <defs>
    <path id="orbit-top" d="M 489 446 A 184 184 0 0 1 857 446"/>
    <path id="orbit-bottom" d="M 481 446 A 192 192 0 0 0 865 446"/>
  </defs>

  <!-- Master wordmark -->
  <g class="master-wordmark" text-anchor="middle">
    <text class="wordmark-name" x="667" y="80" font-size="60">DALLOW</text>
    <text class="wordmark-name" x="667" y="120" font-size="33" letter-spacing="1">EQUIPMENT</text>
    <line class="divider" x1="524" y1="137" x2="809" y2="137"/>
  </g>

  <!-- Option numbers -->
  <g text-anchor="middle">
    <text class="option-number" x="214" y="207">1</text>
    <text class="option-number" x="669" y="207">2</text>
    <text class="option-number" x="1124" y="207">3</text>
  </g>

  <!-- Option 1: white face sticker -->
  <g class="sticker sticker-white" text-anchor="middle">
    <circle class="ring-outer" cx="229" cy="435" r="200"/>
    <circle class="ring-teal" cx="229" cy="435" r="185"/>
    <circle class="face-white" cx="229" cy="435" r="177"/>
    <text class="body-text tagline-dark" x="229" y="333" font-size="17">SOLD AND SERVICED BY</text>
    <text class="wordmark-name" x="229" y="393" font-size="60">DALLOW</text>
    <text class="wordmark-name" x="229" y="436" font-size="33" letter-spacing="1">EQUIPMENT</text>
    <line class="divider" x1="86" y1="454" x2="371" y2="454"/>
    <text class="body-text phone-dark" x="229" y="508" font-size="29">1300 47 82 61</text>
    <text class="body-text tagline-dark" x="229" y="526" font-size="12.5">SALES - PARTS - SERVICE RENTALS</text>
    <text class="body-text tagline-dark" x="229" y="561" font-size="13.5">www.dallowplantco.example</text>
  </g>

  <!-- Option 2: teal face with orbit text -->
  <g class="sticker sticker-teal" text-anchor="middle">
    <path class="orbit-line" d="M 523 329 A 190 190 0 0 0 532 573"/>
    <path class="orbit-line" d="M 823 329 A 190 190 0 0 1 814 573"/>
    <text class="orbit-text"><textPath href="#orbit-top" startOffset="50%">SALES - PARTS - SERVICE RENTALS</textPath></text>
    <text class="orbit-text" font-size="17"><textPath href="#orbit-bottom" startOffset="50%">www.dallowplantco.example</textPath></text>
    <circle class="ring-black" cx="673" cy="446" r="169" stroke-width="6"/>
    <circle class="face-teal" cx="673" cy="446" r="163"/>
    <text class="body-text tagline-light" x="673" y="353" font-size="17">SOLD AND SERVICED BY</text>
    <text class="wordmark-name" x="673" y="417" font-size="60">DALLOW</text>
    <text class="wordmark-name" x="673" y="462" font-size="33" letter-spacing="1">EQUIPMENT</text>
    <line class="divider" x1="532" y1="480" x2="816" y2="480"/>
    <text class="body-text phone-light" x="673" y="537" font-size="31">1300 47 82 61</text>
  </g>

  <!-- Option 3: teal face, heavier ring -->
  <g class="sticker sticker-teal-bold" text-anchor="middle" transform="translate(455 0)">
    <path class="orbit-line" d="M 523 329 A 190 190 0 0 0 532 573"/>
    <path class="orbit-line" d="M 823 329 A 190 190 0 0 1 814 573"/>
    <text class="orbit-text"><textPath href="#orbit-top" startOffset="50%">SALES - PARTS - SERVICE RENTALS</textPath></text>
    <text class="orbit-text" font-size="17"><textPath href="#orbit-bottom" startOffset="50%">www.dallowplantco.example</textPath></text>
    <circle class="ring-black" cx="673" cy="446" r="169" stroke-width="8"/>
    <circle class="face-teal" cx="673" cy="446" r="163"/>
    <text class="body-text tagline-light" x="673" y="353" font-size="17">SOLD AND SERVICED BY</text>
    <text class="wordmark-name" x="673" y="417" font-size="60">DALLOW</text>
    <text class="wordmark-name" x="673" y="462" font-size="33" letter-spacing="1">EQUIPMENT</text>
    <line class="divider" x1="532" y1="480" x2="816" y2="480"/>
    <text class="body-text phone-light" x="673" y="537" font-size="31">1300 47 82 61</text>
  </g>
</svg>
</body>
</html>
```